Restaurant Menu for beach club in Martinique

We would like to set a new design for our Menu. We are a restaurant, and beach club, located in Martinique. Our website is available at : http://www.korivagueplage.net Regards

Colors

Designer to choose colors to be used in the design.

```html
<!DOCTYPE html>
<html lang="fr">
<head>
<meta charset="utf-8">
<title>Kori Vague – Menu</title>
<link href="https://fonts.googleapis.com/css2?family=Josefin+Sans:wght@400;600&family=Italianno&family=Pinyon+Script&display=swap" rel="stylesheet">
<style>
  :root {
    --backdrop: #d9d6d0;
    --cover: #2a2620;
    --cover-edge: #1d1a16;
    --gold: #b8923a;
    --gold-soft: #c9a75a;
    --paper: #f2f0ec;
    --ink: #2b2723;
    --white: #f4f1ea;
  }
  * { box-sizing: border-box; margin: 0; padding: 0; }
  html, body {
    width: 1200px; height: 739px; overflow: hidden;
    background: var(--backdrop);
  }
  .canvas { position: relative; width: 1200px; height: 739px; }

  /* Cover */
  .cover {
    position: absolute; left: 186px; top: 104px; width: 385px; height: 499px;
    background: var(--cover);
    border: 4px solid var(--cover-edge);
  }
  .cover__brand {
    position: absolute; left: 0; right: 0; top: 78px;
    text-align: center;
    font-family: "Josefin Sans", sans-serif; font-weight: 600;
    font-size: 40px; letter-spacing: 2px; color: var(--gold);
  }
  .cover__title {
    position: absolute; left: 0; right: 0; top: 262px;
    text-align: center;
    font-family: "Pinyon Script", cursive; font-size: 50px; color: var(--white);
  }
  .cover__rule {
    position: absolute; left: 97px; top: 333px; width: 184px; height: 7px;
    border-radius: 4px;
    background: linear-gradient(90deg, var(--gold) 0%, var(--gold-soft) 80%, rgba(201,167,90,0) 100%);
  }
  .cover__palms-left { position: absolute; left: 44px; top: 430px; width: 42px; height: 52px; }
  .cover__palms-right { position: absolute; left: 292px; top: 410px; width: 75px; height: 72px; }
  .cover__border-ornament { position: absolute; left: 68px; top: 480px; width: 250px; height: 12px; }

  /* Inside page */
  .page {
    position: absolute; left: 628px; top: 104px; width: 387px; height: 499px;
    background: var(--cover-edge);
  }
  .page__sheet {
    position: absolute; left: 9px; top: 9px; width: 368px; height: 481px;
    background: var(--paper);
    clip-path: polygon(6% 0, 94% 0, 100% 9%, 100% 92%, 94% 100%, 6% 100%, 0 92%, 0 9%);
  }
  .section-head {
    position: absolute; left: 0; right: 0; top: 29px; height: 30px;
  }
  .section-head__line {
    position: absolute; top: 13px; height: 2px; background: var(--gold);
  }
  .section-head__line--left { left: 5px; width: 57px; }
  .section-head__line--right { left: 257px; width: 60px; }
  .section-head__band {
    position: absolute; left: 74px; width: 180px; height: 29px;
    background: var(--gold); border-radius: 3px;
    font-family: "Josefin Sans", sans-serif; font-weight: 600;
    font-size: 23px; letter-spacing: 1px; color: var(--white);
    text-align: center; line-height: 33px;
  }
  .dish {
    position: absolute; left: 0; width: 368px; text-align: center;
  }
  .dish__name {
    font-family: "Italianno", cursive; font-size: 22px; color: var(--gold);
    line-height: 20px;
  }
  .dish__desc {
    font-family: "Josefin Sans", sans-serif; font-size: 6.2px; color: var(--ink);
    line-height: 9px;
  }
  .dish__price {
    font-family: "Josefin Sans", sans-serif; font-weight: 600; font-size: 8.5px;
    color: var(--gold); line-height: 12px;
  }
  .page__corner { position: absolute; top: 374px; width: 54px; height: 94px; }
  .page__corner--left { left: 6px; }
  .page__corner--right { left: 272px; }
  .page__rule {
    position: absolute; left: 35px; top: 436px; width: 287px; height: 1px; background: var(--gold);
  }
  .page__note {
    position: absolute; left: 0; right: 0; top: 449px; text-align: center;
    font-family: "Josefin Sans", sans-serif; font-style: italic; font-size: 6.5px; color: var(--ink);
  }
</style>
</head>
<body>
<div class="canvas">

  <section class="cover">
    <div class="cover__brand">Kori Vague</div>
    <h1 class="cover__title">Menu</h1>
    <div class="cover__rule"></div>
    <svg class="cover__palms-left" role="img" aria-label="Gold palm tree illustration" viewBox="0 0 10 10" preserveAspectRatio="none"><rect width="10" height="10" fill="#a8853a" opacity="0.55"/></svg>
    <svg class="cover__palms-right" role="img" aria-label="Gold palm trees illustration" viewBox="0 0 10 10" preserveAspectRatio="none"><rect width="10" height="10" fill="#a8853a" opacity="0.55"/></svg>
    <svg class="cover__border-ornament" role="img" aria-label="Gold wave scroll ornament" viewBox="0 0 10 10" preserveAspectRatio="none"><rect width="10" height="10" fill="#a8853a" opacity="0.55"/></svg>
  </section>

  <section class="page">
    <div class="page__sheet">
      <header class="section-head">
        <span class="section-head__line section-head__line--left"></span>
        <h2 class="section-head__band">LES ENTREES</h2>
        <span class="section-head__line section-head__line--right"></span>
      </header>

      <div class="dish" style="top:110px">
        <div class="dish__name">L’ assiette «zen»</div>
        <div class="dish__desc">(nem de gambas, maki au saumon, mini brochette de poulet, samoussa au chèvre frais)</div>
        <div class="dish__price">9,80 €</div>
      </div>
      <div class="dish" style="top:162px">
        <div class="dish__name">Les nems aux deux saumons</div>
        <div class="dish__desc">sauce crémeuse au wasabi et salade de pousses d’épinards</div>
        <div class="dish__price">9,50 €</div>
      </div>
      <div class="dish" style="top:214px">
        <div class="dish__name">La salade du « Périgord »</div>
        <div class="dish__desc">(Salade, roquette, oignons rouges, foie gras maison, gésiers confits, magrets fumés et pommes)</div>
        <div class="dish__price">13,10 €</div>
      </div>
      <div class="dish" style="top:269px">
        <div class="dish__name">Le tartare de loup à la moutarde de Reims</div>
        <div class="dish__desc">sur une gelée de concombres</div>
        <div class="dish__price">10,50 €</div>
      </div>
      <div class="dish" style="top:324px">
        <div class="dish__name">Le bavarois de tomates</div>
        <div class="dish__desc">farci au chèvre frais et jus de betteraves</div>
        <div class="dish__price">8,20 €</div>
      </div>

      <svg class="page__corner page__corner--left" role="img" aria-label="Fine gold tropical flowers and palm leaves" viewBox="0 0 10 10" preserveAspectRatio="none"><rect width="10" height="10" fill="#d8c49a" opacity="0.5"/></svg>
      <svg class="page__corner page__corner--right" role="img" aria-label="Fine gold tropical flowers and palm leaves" viewBox="0 0 10 10" preserveAspectRatio="none"><rect width="10" height="10" fill="#d8c49a" opacity="0.5"/></svg>
      <div class="page__rule"></div>
      <p class="page__note">Tous nos prix sont indiqués en TTC et comprennent la TVA à 5,5 %</p>
    </div>
  </section>

</div>
</body>
</html>
```